VELORIA - Società di servizi per la lettura dei contatori acqua

Abbiamo bisogno di una brochure quadrata da 21x21 cm composta da 6 ante. La nostra società Veloria.Siamo specializzati nella lettura e rilievo dei contatori dell'acqua dei condomini/immobili. Siamo una società di servizi composta da un team di professionisti ed operatori specializzati.
Offriamo soluzioni tecnologiche ed efficaci perchè tempestive e performanti.
VELORIA nasce dalla richiesta del mercato di un soggetto nuovo, indipendente e soprattutto trasversale alle attuali realtà di settore.
VELORIA fornisce alle società di amministrazione condominiale un servizio professionale di lettura e riparto dei consumi acqua tempestivo, preciso ed efficace.
VELORIA propone un servizio innovativo sul mercato, capace di gestire la lettura ed il riparto dei consumi acqua tramite un nuovo modello di service management.
Abbiamo strutturato un servizio innovativo dedicato agli amministratori condominiali.
Effettuiamo la lettura dei consumi reali dei contatori acqua relativi alle singole utenze private e comuni.
Elaboriamo i dati raccolti in tempo reale e predisponiamo il riparto dei consumi acqua.
Gli amministratori dispongono di uno strumento tecnico che consente la corretta ed immediata ripartizione dei consumi idrici.
Il riparto dei consumi viene effettuato esclusivamente tramite letture reali, effettive e certificate delle singole utenze.

Target Market(s)

Amministratori di condominio

Font styles to use
Sans Serif

Colors
ec1f27
5c5c5c

Requirements
Must have
• Abbiamo bisogno di una brochure quadrata da 21x21 cm composta da 6 ante.

```html
<!DOCTYPE html>
<html lang="it">
<head>
<meta charset="UTF-8">
<title>Veloria – Brochure, copertina e retro</title>
<link rel="stylesheet" href="https://fonts.googleapis.com/css2?family=Montserrat:wght@600;700&family=Nunito:wght@400&display=swap">
<style>
  :root {
    --stage: #e5e5e5;
    --panel-dark: #58585b;
    --panel-darker: #3f3f42;
    --panel-light: #ffffff;
    --brand-red: #ec1f27;
    --brand-grey: #5c5c5c;
    --ink: #2a2a2a;
    --white: #ffffff;
  }
  * { box-sizing: border-box; margin: 0; padding: 0; }
  html, body {
    width: 1200px; height: 1200px; overflow: hidden;
    background: var(--stage);
  }
  .spread {
    position: absolute; left: 118px; top: 359px;
    display: flex; gap: 10px;
  }
  .panel {
    position: relative; width: 489px; height: 488px; overflow: hidden;
  }
  .panel--cover { background: var(--panel-dark); }
  .panel--back { background: var(--panel-light); }

  .cover-texture {
    position: absolute; left: 0; top: 0; width: 100%; height: 250px;
    background: linear-gradient(to bottom, var(--panel-darker) 0%, var(--panel-dark) 100%);
  }
  .cover-band {
    position: absolute; left: 140px; bottom: 0; width: 194px; height: 24px;
    background: var(--brand-red);
  }

  .wordmark {
    position: absolute; text-align: center;
    font-family: "Montserrat", sans-serif;
  }
  .wordmark__name {
    display: block; font-weight: 600; font-size: 36px;
    letter-spacing: 2.5px; line-height: 1;
  }
  .wordmark__tagline {
    display: block; font-weight: 700; font-size: 10.5px;
    letter-spacing: 3.1px; line-height: 1; margin-top: 4px;
  }
  .panel--cover .wordmark { left: 0; width: 100%; top: 313px; color: var(--white); }
  .panel--back .wordmark { left: 0; width: 100%; top: 120px; }
  .panel--back .wordmark__name { color: var(--brand-red); }
  .panel--back .wordmark__tagline { color: var(--brand-grey); }

  .back-web {
    position: absolute; left: 0; width: 100%; top: 238px;
    text-align: center; font-family: "Nunito", sans-serif;
    font-size: 11px; color: var(--ink);
  }
  .back-web__mark {
    display: block; width: 20px; height: 20px; margin: 0 auto 6px;
    background: var(--ink); border-radius: 4px;
  }
  .back-contacts {
    position: absolute; left: 0; width: 100%; top: 333px;
    text-align: center; font-family: "Nunito", sans-serif;
    font-size: 11px; line-height: 14px; color: var(--ink);
    font-style: normal;
  }
</style>
</head>
<body>
  <main class="spread">
    <section class="panel panel--cover">
      <div class="cover-texture" role="img" aria-label="Motivo decorativo a onde orizzontali grigio scuro che sfuma verso il basso"></div>
      <div class="wordmark">
        <span class="wordmark__name">VELORIA</span>
        <span class="wordmark__tagline">RILEVAZIONE CONSUMI</span>
      </div>
      <div class="cover-band"></div>
    </section>

    <section class="panel panel--back">
      <div class="wordmark">
        <span class="wordmark__name">VELORIA</span>
        <span class="wordmark__tagline">RILEVAZIONE CONSUMI</span>
      </div>
      <div class="back-web">
        <span class="back-web__mark"></span>
        veloria-servizi.it
      </div>
      <address class="back-contacts">
        Via Lario 12, 25128 Brescia (IT)<br>
        Tel. 030/5550182<br>
        info@veloria-servizi.it
      </address>
    </section>
  </main>
</body>
</html>
```